Web Site Design for a Finance (lending) Company

We are opening a new subsidiary that focuses on lending money in the real estate industry. We need a web site designed to represent the business.

The business is lending money to real estate investors. A typical client/borrower will be looking to borrow money to buy a house, renovate it and then sell it at a profit, all within 12 months or less.

Company name is Brevand Finance. Our logo is attached.

Attached is a general outline for the web site. We're working on writing more text for each page but this should give you enough to get started with some ideas.

Competitor web site that I like a lot (as an example): https://quorvelfunding.com/. Many of the general items on this site match what we will need (description of loan programs, FAQ)

Target Market(s)

Real estate investors (generally individuals or small companies with just a few people) who are buying homes, renovating them and then selling them at a profit.

Industry/Entity Type

Finance

Coding

Coded - Design and coding required

Number of Pages Required

5+ page

Colors

Designer to choose colors to be used in the design.

Requirements
Must have
• Minimalist design. Clean lines without too much clutter. Some stock photography is ok but the photos should not be distracting. They should almost fade in to the background so that user can focus on the key information about what our company does instead. We are a finance company, not a design company, so the information about our products will be more interesting to site visitors than the art.
• Some minimalist examples from Snapboard:
• https://www.snapboard-example.com/explore/minimalist-web-design/
Nice to have
• If you search in seekly for "hard money lenders" you will find many examples of web sites from our competition. I have provided a link above to competitor web site that I like a lot.
• I have attached our logo in EPS format. Logo is green. Web site doesn't have to be green but it should be of a color that will work well with the logo.

```html
<!DOCTYPE html>
<html lang="en">
<head>
<meta charset="utf-8">
<title>Brevand Finance — Lending for Real Estate Investors</title>
<link rel="stylesheet" href="https://fonts.googleapis.com/css2?family=Lato:wght@400;700;900&family=Open+Sans:wght@400;600;700&family=Montserrat:wght@400;500;600&display=swap">
<style>
:root{
  --green:#044f2c;
  --green-dark:#033d22;
  --green-chat:#0a3a23;
  --ink:#333333;
  --muted:#777777;
  --light:#f0f0f0;
  --mid:#d9d9d9;
  --grey-card:#7a7a7a;
  --white:#ffffff;
  --black:#111111;
}
*{box-sizing:border-box;margin:0;padding:0}
html,body{width:1200px;height:2423px;overflow:hidden;background:var(--white)}
body{font-family:"Open Sans",Arial,sans-serif;color:var(--ink);position:relative}
.section{position:relative;width:1200px;overflow:hidden}
.abs{position:absolute}

/* header */
.site-header{height:81px;background:var(--white)}
.brand{left:158px;top:14px;display:flex;align-items:center;gap:10px}
.brand-mark{width:30px;height:30px;background:var(--green)}
.brand-name{font-family:"Lato",sans-serif;font-weight:700;font-size:22px;color:var(--green)}
.call{left:800px;top:18px;display:flex;align-items:center;gap:10px}
.call-icon{width:42px;height:42px;background:var(--green);border-radius:7px;display:flex;align-items:center;justify-content:center}
.call-label{font-family:"Lato",sans-serif;font-weight:900;font-size:27px;line-height:26px;color:var(--green)}
.call-number{font-family:"Lato",sans-serif;font-weight:700;font-size:18px;line-height:20px;color:var(--black)}

/* nav */
.main-nav{height:42px;background:var(--green)}
.nav-links{left:158px;top:0;height:42px;display:flex;align-items:center;gap:28px;list-style:none}
.nav-links li{font-family:"Open Sans",sans-serif;font-weight:700;font-size:13px;color:var(--white)}
.nav-social{left:953px;top:9px;display:flex;gap:5px}
.nav-social span{width:24px;height:24px;background:var(--white);border-radius:3px;display:block}

/* hero */
.hero{height:487px;background:linear-gradient(180deg,#3d3a34 0%,#5b564d 45%,#2c3a2c 85%,#2b4a55 100%)}
.hero-photo{inset:0}
.hero-title{left:0;width:1200px;top:296px;text-align:center;font-family:"Lato",sans-serif;font-weight:700;font-size:42px;line-height:48px;color:var(--white)}
.btn-learn{left:517px;top:303px;width:166px;height:39px;background:var(--green);color:var(--white);font-family:"Open Sans",sans-serif;font-weight:700;font-size:13px;display:flex;align-items:center;justify-content:center}

/* programs */
.programs{height:223px;background:var(--light)}
.program{top:0;height:223px;width:293px;text-align:center}
.program.is-active{background:var(--mid)}
.program-mark{width:170px;height:78px;margin:24px auto 0;background:#8a8a8a;opacity:.55}
.program-text{font-size:10.5px;line-height:17px;color:#555;margin:32px 18px 0}
.program-link{font-size:10.5px;color:#444;margin-top:18px}

/* intro */
.intro{height:493px}
.intro-title{left:158px;top:40px;font-family:"Lato",sans-serif;font-size:31px;line-height:40px;color:var(--green)}
.intro-text{left:158px;width:420px;font-size:13.5px;line-height:24px;color:#888}
.btn-phone{left:160px;top:367px;width:226px;height:48px;background:var(--green);border-radius:4px;color:var(--white);font-family:"Lato",sans-serif;font-weight:900;font-size:19px;display:flex;align-items:center;justify-content:center;gap:6px}
.video-frame{left:627px;top:47px;width:411px;height:381px;border:11px solid var(--green);border-radius:8px;background:linear-gradient(160deg,#e8ecef 0%,#c9d1d6 40%,#6b7f92 70%,#9fb0bd 100%)}
.video-play{left:50%;top:50%;transform:translate(-50%,-50%)}

/* testimonial */
.testimonial{height:279px;background:linear-gradient(90deg,#2a2d2a 0%,#4a4b45 50%,#3a3b36 100%)}
.testimonial-title{left:0;width:1200px;top:42px;text-align:center;font-family:"Montserrat",sans-serif;font-weight:500;font-size:31px;color:var(--white)}
.testimonial-quote{left:220px;width:760px;top:94px;text-align:center;font-size:13.5px;line-height:23px;color:var(--white)}
.avatar{left:571px;top:147px;width:58px;height:58px;border-radius:50%;border:3px solid var(--white);background:#b9a58e}
.testimonial-name{left:0;width:1200px;top:223px;text-align:center;font-size:13.5px;color:var(--white)}

/* news */
.news{height:510px}
.news-title{left:0;width:1200px;top:22px;text-align:center;font-family:"Lato",sans-serif;font-weight:700;font-size:45px;color:var(--ink)}
.news-lead{left:290px;width:620px;top:88px;text-align:center;font-size:13.5px;line-height:24px;color:#555}
.news-card{top:155px;width:312px;height:286px}
.news-image{width:312px;height:213px}
.news-caption{height:73px;padding:10px 6px;background:var(--grey-card);color:var(--white)}
.news-card.is-featured .news-caption{background:var(--green)}
.news-caption h3{font-family:"Montserrat",sans-serif;font-weight:500;font-size:17px;line-height:22px}
.news-caption p{font-size:12px;line-height:14px;margin-top:2px}

/* footer */
.site-footer{height:308px;background:var(--green)}
.footer-col{top:55px}
.footer-col h4{font-family:"Montserrat",sans-serif;font-weight:400;font-size:26px;color:var(--white);margin-bottom:14px}
.footer-col ul{list-style:none}
.footer-col li{font-family:"Montserrat",sans-serif;font-size:16px;line-height:33px;color:var(--white)}
.signup{left:765px;top:110px;display:flex}
.signup-email{width:196px;height:42px;background:var(--white);font-family:"Montserrat",sans-serif;font-size:13px;color:#444;padding:13px 12px}
.signup-btn{width:110px;height:42px;background:var(--black);color:var(--white);font-family:"Montserrat",sans-serif;font-weight:600;font-size:18px;display:flex;align-items:center;justify-content:center}
.footer-social{left:765px;top:172px;display:flex;gap:7px}
.footer-social span{width:33px;height:33px;border:2px solid var(--white);border-radius:50%;display:block}
.footer-rule{left:0;top:245px;width:1200px;height:1px;background:rgba(255,255,255,.25)}
.copyright{left:128px;top:270px;font-family:"Montserrat",sans-serif;font-size:13px;color:var(--white)}
.live-chat{left:751px;top:266px;width:320px;height:42px;background:var(--green-chat);color:var(--white);font-family:"Montserrat",sans-serif;font-size:13px;display:flex;align-items:center;justify-content:space-between;padding:0 12px}
.chat-controls{display:flex;gap:8px}
.chat-controls span{width:16px;height:16px;background:var(--white);border-radius:3px;display:block}
</style>
</head>
<body>

<header class="section site-header">
  <div class="abs brand"><span class="brand-mark"></span><span class="brand-name">Brevand Finance</span></div>
  <div class="abs call">
    <span class="call-icon">
      <svg width="24" height="24" viewBox="0 0 24 24"><path fill="#fff" d="M6.6 10.8c1.4 2.8 3.8 5.1 6.6 6.6l2.2-2.2c.3-.3.7-.4 1-.2 1.1.4 2.3.6 3.6.6.6 0 1 .4 1 1V20c0 .6-.4 1-1 1C10.6 21 3 13.4 3 4c0-.6.4-1 1-1h3.5c.6 0 1 .4 1 1 0 1.3.2 2.5.6 3.6.1.3 0 .7-.2 1z"/></svg>
    </span>
    <div><div class="call-label">CALL US</div><div class="call-number">555-014-LOAN (5626)</div></div>
  </div>
</header>

<nav class="section main-nav">
  <ul class="abs nav-links"><li>HOME</li><li>ABOUT US</li><li>LOAN</li><li>RESOURCES</li><li>CONTACT US</li></ul>
  <div class="abs nav-social"><span></span><span></span><span></span></div>
</nav>

<section class="section hero">
  <div class="abs hero-photo" role="img" aria-label="Dusk photo of a modern villa with palm trees and a pool, darkened"></div>
  <h1 class="abs hero-title" style="top:178px">The Nation’s Premier Lender<br>for Real Estate Investors</h1>
  <a class="abs btn-learn">LEARN MORE</a>
</section>

<section class="section programs">
  <div class="abs program" style="left:158px">
    <div class="program-mark" role="img" aria-label="Fix N Flip program wordmark under a roof outline"></div>
    <p class="program-text">Short Term Financing for the Purchase and Rehab of Single-Family Properties</p>
    <p class="program-link">Learn More</p>
  </div>
  <div class="abs program is-active" style="left:452px">
    <div class="program-mark" role="img" aria-label="Rental program wordmark under a roof outline"></div>
    <p class="program-text">Long Term Financing for Single Properties and Portfolios of Single-Family Rentals</p>
    <p class="program-link">Learn More</p>
  </div>
  <div class="abs program" style="left:745px">
    <div class="program-mark" role="img" aria-label="Multifamily program wordmark with building outline"></div>
    <p class="program-text" style="margin-top:22px">Purchase or Refinance 5+ Unit Properties with Rehab<br>Short Term, Interest-Only Financing</p>
    <p class="program-link">Learn More</p>
  </div>
</section>

<section class="section intro">
  <h2 class="abs intro-title">Let us be the stepping stone<br>to the home of your dreams.</h2>
  <p class="abs intro-text" style="top:142px">Et harum quidem rerum facilis est et expedita distinctio. Nam libero tempore, cum soluta nobis est eligendi optio cumque nihil impedit quo minus id quod maxime placeat facere possimus, omnis voluptas assumenda est, omnis dolor repellendus.</p>
  <p class="abs intro-text" style="top:262px">Temporibus autem quibusdam et aut officiis debitis aut rerum necessitatibus saepe eveniet ut et voluptates repudiandae sint et molestiae non recusandae.</p>
  <a class="abs btn-phone">
    <svg width="16" height="16" viewBox="0 0 24 24"><rect x="1" y="1" width="22" height="22" rx="4" fill="#fff"/><path fill="#044f2c" d="M7.5 10.8c1.2 2.4 3.2 4.4 5.7 5.7l1.9-1.9c.2-.2.6-.3.9-.2.9.3 2 .5 3 .5v3.1c0 .5-.4.8-.8.8C10.4 18.8 5.2 13.6 5.2 5.8c0-.5.3-.8.8-.8h3.1c0 1.1.2 2.1.5 3.1.1.3 0 .6-.2.8z"/></svg>
    555-014-LOAN (5626)
  </a>
  <div class="abs video-frame" role="img" aria-label="Video still of a couple viewing a new white house">
    <svg class="abs video-play" width="66" height="66" viewBox="0 0 66 66"><circle cx="33" cy="33" r="29" fill="rgba(0,0,0,.15)" stroke="#fff" stroke-width="5"/><path d="M26 20 L48 33 L26 46 Z" fill="#fff"/></svg>
  </div>
</section>

<section class="section testimonial" role="img" aria-label="Dimmed photo of a bright living room with fireplace behind client testimonial">
  <h2 class="abs testimonial-title">See What Our Clients Have to Say</h2>
  <p class="abs testimonial-quote">The most unbelievable program we have ever seen! Our house was paid for after 11 years. The best part is, it was all free. Reid is amazing!</p>
  <div class="abs avatar" role="img" aria-label="Client portrait"></div>
  <p class="abs testimonial-name">-Dana, Maplecrest, MO</p>
</section>

<section class="section news">
  <h2 class="abs news-title">LATEST NEWS</h2>
  <p class="abs news-lead">Lorem ipsum dolor sit amet, consectetuer adipiscing elit, sed diam nonummy nibh euismod tincidunt ut laoreet dolore magna aliquam erat volutpat.</p>
  <article class="abs news-card is-featured" style="left:129px">
    <div class="news-image" role="img" aria-label="Person writing in a notebook beside a coffee cup" style="background:linear-gradient(135deg,#e9e9e6,#b9b6b0 60%,#7a7066)"></div>
    <div class="news-caption"><h3>IDENTIFY THE ISSUES</h3><p>We help you break down your legal problems</p></div>
  </article>
  <article class="abs news-card" style="left:445px">
    <div class="news-image" role="img" aria-label="Smiling couple reviewing documents together" style="background:linear-gradient(135deg,#f2efe9,#d8c7b4 55%,#9aa6b3)"></div>
    <div class="news-caption"><h3>STRUCTURED ADVICE</h3><p>We give you clear legal advice about your options</p></div>
  </article>
  <article class="abs news-card" style="left:760px">
    <div class="news-image" role="img" aria-label="Hands typing on a laptop at a wooden desk" style="background:linear-gradient(135deg,#d6dde4,#8b7a6a 60%,#4e3a2c)"></div>
    <div class="news-caption"><h3>RESEARCH &amp; ANALYSIS</h3><p>We examine your case to find the best solution for you</p></div>
  </article>
</section>

<footer class="section site-footer">
  <div class="abs footer-col" style="left:126px"><h4>OUR INFO</h4><ul><li>HOMEPAGE</li><li>ABOUT US</li><li>HIRING</li></ul></div>
  <div class="abs footer-col" style="left:305px"><h4>BOOKING</h4><ul><li>BOOKING PAGE</li><li>BLOG</li></ul></div>
  <div class="abs footer-col" style="left:480px"><h4>ADDITIONAL LINKS</h4><ul><li>GIFT CARD</li><li>HELP</li><li>WE’RE GREEN</li></ul></div>
  <div class="abs footer-col" style="left:765px"><h4>STAY CONNECTED</h4></div>
  <div class="abs signup"><div class="signup-email">EMAIL</div><div class="signup-btn">SIGN UP</div></div>
  <div class="abs footer-social"><span></span><span></span><span></span><span></span></div>
  <div class="abs footer-rule"></div>
  <p class="abs copyright">Copyright Brevand @2017</p>
  <div class="abs live-chat"><span>Live Chat</span><span class="chat-controls"><span></span><span></span></span></div>
</footer>

</body>
</html>
```